I need a folder to put papers in when I am scheduling patients for surgery. The information is general, such as costs, consent forms etc. The folder is designed to give the patient these papers in a neat manner. The cover of the folder needs to use my brand and perhaps create some interest when it is sitting on their kitchen bench with visitors and family. I'll attach a typical template for a folder. It needs to be stylish, classic and professional, as I am about to operate on the person's eye. <br/>I would like my logo included. I'll also attach a photo which is on my website which might work to wrap around the folder. The website address is bramwelkoske.com.au and you can see the way the image is used there on most of the pages as a banner. My profile photo could possibly used as well. Perhaps on the back, but if it looks strange then that is not necessary. The contact information need not be on the folder. Just Dr Lars Brimwell, Ophthalmic Surgeon. Finally, our brand slogan is. "The world's a beautiful place, see it clearly". This could also be on it. Again, this all needs to be professional looking. <br/>I've attached all our previous design jobs, 2 profile pictures, and the image that I think would work. Please also look at the website. <br/><br/>The second part of the project is to create a business card for my practice manager. Her name is Fiona Pelkrest<br/>It should include<br/>Fiona Pelkrest (BCom)<br/>Practice Manager for Dr Lars Brimwell<br/>Ophthalmic Surgeon <br/><br/>Then all the details which are on our current business card<br/><br/><br/><br/><br/>

Contact Information for Business Card

Just match the business cards I already have, but use the details above

Colors

Designer to choose colors to be used in the design.

```html
<!DOCTYPE html>
<html lang="en">
<head>
<meta charset="utf-8">
<title>Dr Lars Brimwell – Patient Folder</title>
<link rel="stylesheet" href="https://fonts.googleapis.com/css2?family=Open+Sans:wght@400;600;700&family=Roboto:wght@700&display=swap">
<style>
  :root {
    --brand-blue: #1b7bc0;
    --brand-blue-deep: #0d5d9a;
    --brand-blue-light: #2792d3;
    --stripe-grey: #4a4d50;
    --paper: #ffffff;
    --paper-shade: #dfe1e3;
    --text-grey: #5b5e61;
    --backdrop: #d6d7d8;
    --sunset-sky: #a88a5c;
    --sunset-sea: #2a2620;
  }
  * { box-sizing: border-box; margin: 0; padding: 0; }
  html, body { width: 1200px; height: 847px; overflow: hidden; }
  body {
    background: var(--backdrop);
    font-family: "Open Sans", sans-serif;
    position: relative;
  }
  .folder-spread {
    position: absolute;
    left: 80px; top: 56px;
    width: 1040px; height: 735px;
    display: flex;
    box-shadow: 0 18px 40px rgba(0,0,0,0.25);
  }
  .folder-panel {
    position: relative;
    width: 520px; height: 735px;
    overflow: hidden;
    background: var(--paper);
  }
  .folder-panel--back {
    background: linear-gradient(120deg, var(--paper) 20%, var(--paper-shade) 100%);
  }
  .panel-art { position: absolute; inset: 0; width: 100%; height: 100%; }
  .brand {
    position: absolute;
    display: flex;
    align-items: center;
    gap: 14px;
  }
  .brand__mark {
    width: 40px; height: 40px;
    border-radius: 50%;
    background: var(--brand-blue);
    flex-shrink: 0;
  }
  .brand__name {
    font-weight: 600;
    font-size: 30px;
    color: var(--brand-blue);
    line-height: 1;
  }
  .brand__role {
    font-weight: 700;
    font-size: 10px;
    color: var(--text-grey);
    margin-top: 5px;
  }
  .brand__credentials {
    font-weight: 400;
    font-size: 8px;
    color: var(--text-grey);
  }
  .folder-panel--back .brand { left: 70px; top: 70px; }
  .folder-panel--front .brand { left: 60px; top: 70px; }
  .profile-photo {
    position: absolute;
    left: 300px; top: 280px;
    width: 190px; height: 160px;
    border: 5px solid var(--paper);
    background: linear-gradient(135deg, #cfd6d8 0%, #9fb3bf 50%, #2c2f36 100%);
  }
  .slogan {
    position: absolute;
    left: 0; right: 0; top: 560px;
    text-align: center;
    font-family: "Roboto", sans-serif;
    font-weight: 700;
    font-size: 27px;
    line-height: 1.35;
    color: var(--paper);
  }
</style>
</head>
<body>
  <main class="folder-spread">
    <section class="folder-panel folder-panel--back">
      <svg class="panel-art" viewBox="0 0 520 735" preserveAspectRatio="none" aria-hidden="true">
        <defs>
          <linearGradient id="backBlue" x1="0" y1="0" x2="1" y2="1">
            <stop offset="0" stop-color="#2a98d8"/>
            <stop offset="1" stop-color="#0c5b98"/>
          </linearGradient>
        </defs>
        <polygon points="0,575 520,300 520,320 0,590" fill="var(--stripe-grey)"/>
        <polygon points="0,592 520,322 520,735 0,735" fill="url(#backBlue)"/>
      </svg>
      <div class="brand">
        <span class="brand__mark"></span>
        <div>
          <p class="brand__name">Dr Lars Brimwell</p>
          <p class="brand__role">Ophthalmic Surgeon</p>
          <p class="brand__credentials">MBBS (Hons) MMed FRANZCO</p>
        </div>
      </div>
      <div class="profile-photo" role="img" aria-label="Portrait photograph of the surgeon in a dark blazer"></div>
    </section>

    <section class="folder-panel folder-panel--front">
      <svg class="panel-art" viewBox="0 0 520 735" preserveAspectRatio="none" aria-hidden="true">
        <defs>
          <linearGradient id="sunset" x1="0" y1="0" x2="0" y2="1">
            <stop offset="0" stop-color="#6f675a"/>
            <stop offset="0.35" stop-color="var(--sunset-sky)"/>
            <stop offset="0.5" stop-color="#8a6c44"/>
            <stop offset="1" stop-color="var(--sunset-sea)"/>
          </linearGradient>
        </defs>
        <polygon points="0,300 520,120 520,130 0,345" fill="var(--brand-blue)"/>
        <g role="img" aria-label="Photograph of the sun setting over the ocean">
          <polygon points="0,348 520,133 520,735 0,735" fill="url(#sunset)"/>
        </g>
      </svg>
      <div class="brand">
        <span class="brand__mark"></span>
        <div>
          <p class="brand__name">Dr Lars Brimwell</p>
          <p class="brand__role">Ophthalmic Surgeon</p>
          <p class="brand__credentials">MBBS (Hons) MMed FRANZCO</p>
        </div>
      </div>
      <p class="slogan">The World's a Beautiful Place,<br>See it Clearly</p>
    </section>
  </main>
</body>
</html>
```